Gym Wall Story Feature-- Long Horizontal design for the full-width of the gym wall

We need a horizontal, LONG, story poster/display that artfully tells our gym's story using ALL of the attached information and photographs. I've also included where this display will go in our gym (aligned with, and under the trophies.) Please incorporate the color scheme of white, light grey, dark grey, and orange.

Thanks!

Target Market(s)

Upscale, exclusive, hip gym community

Industry/Entity Type

Gym

Font styles to use
Sans Serif

Colors
ffffff
000000
aaaaaa
5c5c5c
f78f20
e9e9e9

Requirements
Must have
• All images and text provided in the attachments. Clean, modern, design. MOSTLY white with just a couple pops of orange and light grey. text should be black or charcoal and easy to read. We would like to have our logo incorporated as well.
Nice to have
• Clean, stream-line look, nothing too busy or crowded.
Should not have
• Too busy, slanted lines, weird fonts, misalignment.

```html
<!DOCTYPE html>
<html lang="en">
<head>
<meta charset="utf-8">
<title>How Did The Method Start?</title>
<link rel="stylesheet" href="https://fonts.googleapis.com/css2?family=Lato:wght@300;400;700;900&display=swap">
<style>
  :root {
    --white: #ffffff;
    --black: #000000;
    --charcoal: #3f3f3f;
    --grey-dark: #5c5c5c;
    --grey-mid: #aaaaaa;
    --grey-light: #e9e9e9;
    --grey-faint: #f3f3f3;
    --orange: #f78f20;
    --text-body: #7a7a7a;
  }
  * { box-sizing: border-box; margin: 0; padding: 0; }
  html, body { width: 1200px; height: 546px; overflow: hidden; background: var(--white); }
  body { font-family: 'Lato', sans-serif; color: var(--charcoal); }
  .story-wall { position: relative; width: 1200px; height: 546px; overflow: hidden; background: var(--white); }

  .backdrop { position: absolute; background: linear-gradient(180deg, var(--grey-faint), #ececec); }
  .backdrop--left { left: 0; top: 88px; width: 300px; height: 458px; border-radius: 0 120px 0 0; opacity: .8; }
  .backdrop--right { right: 0; top: 96px; width: 190px; height: 450px; border-radius: 110px 0 0 0; opacity: .8; }

  .timeline { position: absolute; left: 0; top: 0; }

  .photo { position: absolute; background: linear-gradient(160deg, #8a8a8a, #3a3a3a); }
  .photo--early { left: 125px; top: 102px; width: 98px; height: 156px; background: linear-gradient(160deg, #9a9a9a, #2e2e2e); }
  .photo--stage { left: 449px; top: 326px; width: 114px; height: 148px; background: linear-gradient(160deg, #a0644a, #2a1c18); }
  .photo--today { left: 765px; top: 103px; width: 104px; height: 153px; background: linear-gradient(160deg, #c9b94c, #3a3a3a); }

  .entry { position: absolute; font-size: 7.8px; line-height: 1.45; color: var(--text-body); font-weight: 400; }
  .entry p + p { margin-top: 8px; }
  .entry strong { color: var(--charcoal); font-weight: 700; font-size: 8px; }
  .entry--1973 { left: 234px; top: 100px; width: 186px; }
  .entry--1981 { left: 575px; top: 327px; width: 160px; }
  .entry--2015 { left: 878px; top: 102px; width: 180px; }

  .year { position: absolute; font-weight: 700; font-size: 19px; color: var(--orange); }
  .year--1973 { left: 95px; top: 307px; }
  .year--1981 { left: 416px; top: 262px; }
  .year--2015 { left: 739px; top: 304px; }

  .activity-strip { position: absolute; left: 468px; top: 84px; width: 226px; height: 46px;
    background: linear-gradient(90deg, var(--grey-dark), #3a3a3a); opacity: .85; border-radius: 2px; }

  .quote { position: absolute; left: 456px; top: 132px; width: 251px; height: 97px; background: var(--orange);
    box-shadow: 0 2px 4px rgba(0,0,0,.15); display: flex; align-items: center; justify-content: center;
    text-align: center; color: var(--white); font-size: 12.6px; font-weight: 300; line-height: 1.35; padding: 0 30px; }
  .quote-tail { position: absolute; left: 456px; top: 228px; }

  .titles-heading { position: absolute; left: 878px; top: 155px; font-size: 9px; font-weight: 700; color: var(--charcoal); letter-spacing: .1px; }
  .titles { position: absolute; left: 879px; top: 171px; list-style: none; }
  .titles li { display: flex; gap: 2px; height: 21px; margin-bottom: 9px; font-size: 6.6px; }
  .titles .titles-year { width: 42px; background: var(--orange); color: var(--charcoal); display: flex; align-items: center; justify-content: center; }
  .titles .titles-name { width: 125px; border: 1px solid var(--grey-mid); background: var(--white); color: var(--charcoal); display: flex; align-items: center; justify-content: center; }

  .headline { position: absolute; left: 69px; top: 349px; font-size: 37px; line-height: 42px; font-weight: 700; color: var(--charcoal); letter-spacing: .3px; }
  .headline .accent { color: var(--orange); }
  .headline .light { color: var(--orange); font-weight: 300; display: block; }

  .tag-cloud { position: absolute; left: 0; top: 0; font-weight: 400; color: #6a6a6a; line-height: 1; }
  .tag { position: absolute; white-space: nowrap; }
  .tag--y1981 { left: 765px; top: 354px; font-size: 52px; }
  .tag--title1 { left: 886px; top: 383px; font-size: 22px; }
  .tag--y1973 { left: 939px; top: 354px; font-size: 26px; }
  .tag--first { left: 770px; top: 398px; font-size: 33px; font-weight: 900; color: var(--orange); }
  .tag--past70 { left: 942px; top: 400px; font-size: 17px; }
  .tag--title2 { left: 942px; top: 416px; font-size: 17px; }
  .tag--last { left: 799px; top: 428px; font-size: 33px; font-weight: 900; color: var(--orange); }
  .tag--y2015 { left: 911px; top: 424px; font-size: 52px; }
</style>
</head>
<body>
<main class="story-wall">
  <div class="backdrop backdrop--left" role="img" aria-label="Faint grey silhouette of a lifter in the background"></div>
  <div class="backdrop backdrop--right" role="img" aria-label="Faint grey silhouette of a lifter in the background"></div>

  <svg class="timeline" width="1200" height="546" viewBox="0 0 1200 546" aria-hidden="true">
    <g stroke="#5c5c5c" stroke-width="1" fill="none">
      <line x1="67" y1="295" x2="1132" y2="295"/>
      <polyline points="125,122 117,122 117,295"/>
      <polyline points="439,295 439,448 449,448"/>
      <polyline points="765,125 760,125 760,295"/>
    </g>
    <g fill="#5c5c5c">
      <circle cx="117" cy="295" r="7"/>
      <circle cx="439" cy="295" r="7"/>
      <circle cx="760" cy="295" r="7"/>
      <circle cx="144" cy="295" r="2.3"/><circle cx="171" cy="295" r="2.3"/><circle cx="198" cy="295" r="2.3"/>
      <circle cx="225" cy="295" r="2.3"/><circle cx="252" cy="295" r="2.3"/><circle cx="279" cy="295" r="2.3"/>
      <circle cx="306" cy="295" r="2.3"/><circle cx="333" cy="295" r="2.3"/><circle cx="360" cy="295" r="2.3"/>
      <circle cx="387" cy="295" r="2.3"/><circle cx="414" cy="295" r="2.3"/>
      <circle cx="466" cy="295" r="2.3"/><circle cx="493" cy="295" r="2.3"/><circle cx="520" cy="295" r="2.3"/>
      <circle cx="547" cy="295" r="2.3"/><circle cx="574" cy="295" r="2.3"/><circle cx="601" cy="295" r="2.3"/>
      <circle cx="628" cy="295" r="2.3"/><circle cx="655" cy="295" r="2.3"/><circle cx="682" cy="295" r="2.3"/>
      <circle cx="709" cy="295" r="2.3"/><circle cx="736" cy="295" r="2.3"/>
      <circle cx="787" cy="295" r="2.3"/><circle cx="814" cy="295" r="2.3"/><circle cx="841" cy="295" r="2.3"/>
      <circle cx="868" cy="295" r="2.3"/><circle cx="895" cy="295" r="2.3"/><circle cx="922" cy="295" r="2.3"/>
      <circle cx="949" cy="295" r="2.3"/><circle cx="976" cy="295" r="2.3"/><circle cx="1003" cy="295" r="2.3"/>
      <circle cx="1030" cy="295" r="2.3"/><circle cx="1057" cy="295" r="2.3"/>
    </g>
  </svg>

  <div class="photo photo--early" role="img" aria-label="Black and white photo of young Dorian Vale posing at a body-building contest"></div>
  <section class="entry entry--1973">
    <p>The Method began with body builder and personal trainer, Dorian Vale. Dorian had a passion for fitness early on and opened his first gym in 1960.</p>
    <p><strong>Shortly after, Dorian won Mr. Eastern State.</strong></p>
    <p>Dorian's body-building career looked promising until one evening he was robbed and shot in the chest. As a result, Dorian suffered from nerve damage in the arm and figured at the age of 34, his weight lifting days were over.</p>
  </section>
  <span class="year year--1973">1973</span>

  <div class="activity-strip" role="img" aria-label="Row of small workout silhouettes: cycling, push-up, pull-up, bench press and running"></div>
  <blockquote class="quote">“I thought I was through and couldn’t continue lifting but the method changed everything.”</blockquote>
  <svg class="quote-tail" width="40" height="50" viewBox="0 0 40 50" aria-hidden="true">
    <polygon points="12,0 38,0 21,48" fill="#f78f20"/>
  </svg>
  <span class="year year--1981">1981</span>

  <div class="photo photo--stage" role="img" aria-label="Color photo of Dorian Vale flexing on stage at a competition"></div>
  <section class="entry entry--1981">
    <p>Dorian started with 2-pound weights and changed his whole training technique.</p>
    <p>No more bouncing or slinging, just steady and controlled movements. Through hard work and consistency, Dorian started shaping up his upper-body again.</p>
    <p><strong>Shortly after turning 40, Dorian won the National Mr. Atlantic competition.</strong></p>
  </section>

  <div class="photo photo--today" role="img" aria-label="Photo of Dorian Vale standing in his gym beside the dumbbell rack"></div>
  <section class="entry entry--2015">
    <p>Through his experiences, Dorian created The Method; a system that helps individuals develop a fundamentally sound workout regimen and accountability system.</p>
  </section>
  <h3 class="titles-heading">NATIONAL CHAMPIONSHIPS WON:</h3>
  <ul class="titles">
    <li><span class="titles-year">1981</span><span class="titles-name">Won Past 40 Mr. Atlantic</span></li>
    <li><span class="titles-year">1999</span><span class="titles-name">Won Past 60 Mr. Atlantic</span></li>
    <li><span class="titles-year">1996</span><span class="titles-name">Won Past 50 Mr. Atlantic</span></li>
    <li><span class="titles-year">2009</span><span class="titles-name">Won Past 70 Mr. Atlantic</span></li>
  </ul>
  <span class="year year--2015">2015</span>

  <h1 class="headline"><span class="accent">HOW</span> DID THE<span class="light">METHOD</span>START?</h1>

  <div class="tag-cloud" aria-label="Highlights">
    <span class="tag tag--y1981">1981</span>
    <span class="tag tag--y1973">1973</span>
    <span class="tag tag--title1">MR. ATLANTIC</span>
    <span class="tag tag--first">DORIAN</span>
    <span class="tag tag--past70">WON PAST 70</span>
    <span class="tag tag--title2">MR. ATLANTIC</span>
    <span class="tag tag--last">VALE</span>
    <span class="tag tag--y2015">2015</span>
  </div>
</main>
</body>
</html>
```